Dreiköpfiges Expertenteam sucht Leporello für Workshop zu Konfliktlösung
Zielgruppe
Wir sind ein dreiköpfiges Expertenteam bestehend aus einem Facharzt für Psychosomatische Medizin und Psychotherapie, Wirtschaftsprüfer und einer Mediatorin und suchen ein ansprechendes Design für ein Workshop - Angebot zu tiefenpsychologischer Konfliktlösung, das sich an Fach – und Führungskräfte aus Wirtschaft, Recht, Politik und Soziales; Rechtsanwälte, Berater, Steuerberater, Wirtschaftsprüfer, Manager, Vorstände, u.v.m. richtet.
Aufgabenstellung
Die technischen Spezifikationen und strukturellen Spezifikationen habe ich im Word - Dokument '1-' hochgeladen. Wir möchten einen Leporello entwerfen lassen, der sechs Spalten hat in Wickelfalz
• Ausführung Hochformat
• geschlossenes Endformat DIN lang plus (10,5 x 21 cm)
• Seitenanzahl 6
Ich habe das KRVO - Seminar angehangen, da mir dieses Design und Farbgebung sehr gut gefallen hat.
NEU: Ich habe nun seit Projektbeginn erfahren, dass es bei der Masse an Infos schwierig ist sie alle auf sechs Seiten unterzubringen. Ich habe nun die Gliederung ein bisschen verändert und die Texte zu den Referenten gekürzt, bitte um Beachtung.
Aber generell sind wir was die Gestaltung, Gliederung und evtl. Kürzung von Infos angeht sehr offen und freuen uns auf Eure Ideen.
NEU 2: Achtung - kürzere Vitas.

```html
<!DOCTYPE html>
<html lang="de">
<head>
<meta charset="utf-8">
<title>Averta Wirtschaftsmediation – Faltblatt Workshop</title>
<link href="https://fonts.googleapis.com/css2?family=Arimo:wght@400;700&family=Open+Sans:wght@600;700&display=swap" rel="stylesheet">
<style>
:root{
  --backdrop:#5a5a5a;
  --paper:#ffffff;
  --gold:#c6a63b;
  --gold-light:#dcc684;
  --ink:#333333;
  --muted:#777777;
  --pale:#c9c9c9;
  --line:#bdbdbd;
  --photo-tone:#8a6a4a;
}
*{box-sizing:border-box;margin:0;padding:0}
html,body{width:971px;height:1200px;overflow:hidden;background:var(--backdrop);font-family:"Arimo",Arial,sans-serif;color:var(--ink)}
.sheet{position:absolute;left:62px;width:837px;background:var(--paper);overflow:hidden}
.sheet-outside{top:26px;height:560px}
.sheet-inside{top:607px;height:556px}
.abs{position:absolute}
p,li{font-size:7.7px;line-height:12.6px}
.tiny p,.tiny li{font-size:5.6px;line-height:8.3px}

/* Außenseite */
.photo-frame{left:0;top:0;width:298px;height:79px;background:var(--pale)}
.venue-photo{left:33px;top:0;width:222px;height:89px;background:linear-gradient(120deg,#5c4330,var(--photo-tone) 45%,#c9b79a)}
.venue-text{left:31px;top:108px;width:226px;text-align:justify}
.venue-text h3{font-size:7.7px;font-weight:700;line-height:12.6px}
.venue-link{left:33px;top:216px;width:224px;text-align:right;font-size:5.6px;color:var(--muted)}
.gold-band{left:0;top:238px;width:837px;height:93px;background:var(--gold)}
.map{left:86px;top:238px;width:169px;height:93px;background:linear-gradient(135deg,#e6e6e6,#bdbdbd)}
.contact{left:276px;top:249px;width:256px;text-align:center;color:#fff}
.contact p{font-size:7.7px;line-height:12.4px}
.contact strong{font-weight:700}
.cover-title{left:575px;top:247px;width:245px;text-align:center;color:#fff}
.cover-title h1{font-family:"Open Sans",Arial,sans-serif;font-size:10.3px;font-weight:700;line-height:16px}
.cover-title p{font-size:7.8px;line-height:12.6px;margin-top:10px}
.brand{left:590px;top:84px;width:218px;text-align:right}
.brand-name{font-size:33px;font-weight:400;letter-spacing:4px;color:#2e2e2e;line-height:1}
.brand-sub{font-size:10.5px;letter-spacing:3.6px;color:#2e2e2e;margin-top:2px}
.directions{left:31px;top:362px;width:232px}
.directions h3{font-size:7.7px;font-weight:700;line-height:12.6px}
.directions .gap{margin-top:10px}
.doctor-address{left:330px;top:441px;width:160px;text-align:center}
.doctor-address p{font-size:6.4px;line-height:10px}
.placeholder-note{left:635px;top:418px;font-size:9px;color:var(--pale)}

/* Innenseite */
.inside-header{left:0;top:0;width:256px;height:61px;background:var(--gold);color:#fff;padding:13px 0 0 31px}
.inside-header h2{font-family:"Open Sans",Arial,sans-serif;font-size:11.3px;font-weight:700;line-height:17px}
.section-title{font-size:7.7px;font-weight:700;color:#555;padding-bottom:2px;margin-bottom:7px;border-bottom:1px solid var(--line);width:62px}
.col-left{left:31px;top:86px;width:226px}
.col-left section{margin-bottom:11px}
.col-left p{text-align:justify}
.col-mid{left:307px;top:86px;width:205px}
.col-mid .section-title{margin-left:66px}
.schedule{display:grid;grid-template-columns:66px 1fr;font-size:7.7px;line-height:12.6px}
.schedule .time{color:var(--gold);font-weight:700}
.registration{left:297px;top:239px;width:218px;height:222px;background:var(--gold);padding:9px 10px;color:#fff}
.registration h3{font-size:7.8px;font-weight:700;padding-bottom:4px;margin-bottom:6px;border-bottom:1px solid var(--gold-light)}
.registration p{font-size:7.2px;line-height:11.6px;color:#fdf8ea}
.registration p+p{margin-top:10px}
.registration strong{color:#fff;font-weight:700}
.speakers-title{left:575px;top:30px;width:100px;font-size:8px}
.speaker{position:absolute;left:575px;width:244px;padding-right:46px}
.speaker h4{font-size:5.8px;font-weight:700;line-height:8.3px}
.portrait-shadow{position:absolute;right:-18px;top:14px;width:40px;height:50px;background:var(--pale)}
.portrait{position:absolute;right:0;top:6px;width:40px;height:50px;background:linear-gradient(160deg,#d8d8d8,#6d6d6d)}
.speaker-1{top:48px}
.speaker-2{top:212px}
.speaker-3{top:376px}
.references{left:575px;top:476px;width:198px}
.references ul{list-style:none}
.references li::before{content:"•";display:inline-block;width:30px}
</style>
</head>
<body>

<div class="sheet sheet-outside">
  <div class="abs photo-frame"></div>
  <div class="abs venue-photo" role="img" aria-label="Foto: Empfangsbereich des Business-Clubs mit Holztheke"></div>
  <div class="abs venue-text">
    <h3>Exklusives und vertrauliches Ambiente im Skyline Club Frankfurt</h3>
    <p>Der Skyline Club Frankfurt zählt zu den bedeutendsten Businessclubs in Europa. In einem exklusiven Ambiente, mit einem professionellen Tagungsmanagement, und einem zuvorkommenden, aber diskreten Service. Ein Ort, an dem Sie sich jederzeit wohlfühlen können, weil stets Ihren Wünschen entsprochen wird.</p>
  </div>
  <div class="abs venue-link">mehr Infos unter: https://www.skylineclub-ffm.de/</div>

  <div class="abs gold-band"></div>
  <div class="abs map" role="img" aria-label="Lageplan der Umgebung des Veranstaltungsortes"></div>
  <div class="abs contact">
    <p><strong>Kontaktdaten</strong></p>
    <p style="margin-top:6px"><strong>Averta Wirtschaftsmediation GmbH</strong></p>
    <p>Lindenweg 14</p>
    <p>60322 Frankfurt am Main</p>
    <p>Tel.: 069 5550 1200</p>
    <p>Email: info@averta-wm.de</p>
  </div>
  <div class="abs cover-title">
    <h1>Konfliktmanagement und<br>Verhandlungstechnik:</h1>
    <p>strategisch-psychologische<br>Perspektiven und Lösungsmöglichkeiten</p>
  </div>

  <div class="abs brand">
    <div class="brand-name">AVERTA</div>
    <div class="brand-sub">Wirtschaftsmediation</div>
  </div>

  <div class="abs directions">
    <h3>Anfahrt</h3>
    <h3>Anreise Auto</h3>
    <p>Über die Stadtautobahn Richtung Zentrum. Beschilderung „Skyline Tower“ folgen und die Tiefgarage P 1 oder P 2 nutzen.</p>
    <p class="gap"><strong>Anreise mit Bus oder Bahn</strong> (S-Bahn-Station)</p>
    <p>Nehmen Sie den Ausgang „Lindenallee“ und gehen Sie bis zum Haupteingang. Folgen Sie dort der Beschilderung „Skyline Club, Ebene 12“.</p>
    <p>Anreise Bahn (Hauptbahnhof)</p>
    <p>Beschilderung „Skyline Tower“ folgen.</p>
  </div>

  <div class="abs doctor-address">
    <p><strong>Dr. med. Lukas Feldner</strong></p>
    <p>Ahornstraße 7</p>
    <p>65193 Wiesbaden</p>
    <p>Tel.: 0611-555 0190</p>
  </div>

  <div class="abs placeholder-note">Bild und Spruch ?</div>
</div>

<div class="sheet sheet-inside">
  <div class="abs inside-header"><h2>Konfliktmanagement und<br>Verhandlungstechnik</h2></div>

  <div class="abs col-left">
    <section>
      <h3 class="section-title">Ihr Nutzen</h3>
      <p>Konflikte können belastend und reine Energiefresser in Privat – und Berufsleben sein. In unserem Workshop wollen wir Ihren Umgang in und mit konfliktgeladenen Situationen schulen. Durch unsere interdisziplinäre Expertise laden wir Sie ein, eine neue Sichtweise auf die Dynamiken und Muster in Konflikten zu gewinnen und neue Formen der Streitanalyse und -beilegung zu erproben, um Ihr Verhandlungsgeschick auch in belastenden Situationen nicht zu verlieren.</p>
    </section>
    <section>
      <h3 class="section-title">Ziele</h3>
      <p>Grundkenntnisse der tiefenpsychologischen Mechanismen und Ursachen bei Konflikten aufbauen. Sich einen sensibilisierenden Umgang in Konfliktsituationen im Beruf – und Arbeitsleben aneignen. Werkzeuge und Methoden zur Analyse, Schlichtung, Deeskalation und/oder Intervention erlernen. Verhandlungsstrategien kennenlernen.</p>
    </section>
    <section>
      <h3 class="section-title">Zielgruppe</h3>
      <p>Fach – und Führungskräfte aus Wirtschaft, Recht, Politik und Soziales; Rechtsanwälte, Berater, Steuerberater, Wirtschaftsprüfer, Manager, Vorstände, u.v.m.</p>
    </section>
    <section>
      <h3 class="section-title">Wieviel</h3>
      <p>650 € pro Person zzgl. MwSt.</p>
      <p>Der Preis beinhaltet Pausensnacks sowie Kaffee, Tee und Softdrinks, sowie die Seminarunterlagen.</p>
    </section>
    <section>
      <h3 class="section-title">Wo</h3>
      <p>Skyline Club Frankfurt GmbH<br>Skyline Tower, Ebene 12<br>Lindenallee 40<br>60311 Frankfurt am Main</p>
    </section>
  </div>

  <div class="abs col-mid">
    <h3 class="section-title">Ablauf</h3>
    <div class="schedule">
      <span class="time">14.00 – 15.15</span><span>Theoretische Grundlagen zur tiefenpsychologischen Konfliktlösung</span>
      <span class="time">15.15 – 15.30</span><span>Pause</span>
      <span class="time">15.30 – 16.30</span><span>Vorstellung und Erlernen von Methoden tiefenpsychologischer Konfliktlösung anhand von Fallbeispielen</span>
      <span class="time">16.30 – 17.00</span><span>Pause</span>
      <span class="time">17.00 – 18.30</span><span>Reflexion, Methodenvertiefung und Erfahrungsberichte</span>
    </div>
  </div>

  <div class="abs registration">
    <h3>Organisation und Anmeldung</h3>
    <p>Unsere Workshops finden mehrmals im Jahr in Kleingruppen bis zu max. 12 Personen statt. Wir freuen uns, Ihnen den Workshop in einem vertraulichen und exklusiven Ambiente anbieten zu können. Der Skyline Club Frankfurt überzeugt durch seinen erstklassigen und diskreten Service, seine exzellente Clubgastronomie und die zentrale Lage in der Innenstadt.</p>
    <p>Nach Anmeldung über Email senden wir Ihnen die Termine der Workshops zur Auswahl zu, unter denen Sie sich den passenden auswählen. Erst danach erfolgt die Buchung und Sie erhalten vor dem Seminarbeginn die Rechnung. Anmeldungen nehmen wir gerne unter der folgenden Adresse entgegen: <strong>anmeldung@averta-wm.de</strong></p>
  </div>

  <h3 class="abs section-title speakers-title">Die Referenten</h3>

  <div class="speaker speaker-1 tiny">
    <div class="portrait-shadow"></div>
    <div class="portrait" role="img" aria-label="Porträtfoto des Referenten"></div>
    <h4>Dr. med. Lukas Feldner</h4>
    <p>Studium der Humanmedizin und Approbation als Arzt, anschließend klinische Jahre in mehreren Fachabteilungen. Seit vielen Jahren niedergelassen in eigener Praxis als Facharzt für Psychosomatische Medizin und Psychotherapie. Anerkannter Leiter von Balintgruppen und erfahrener Supervisor. Langjährige Lehrtätigkeit in der ärztlichen Fort- und Weiterbildung, insbesondere zur psychosomatischen Grundversorgung und zur Gruppentherapie. Schulung einer großen Zahl von Ärztinnen und Ärzten in der Gesprächsführung mit belasteten Patienten. Dozent in Kursen zum Umgang mit chronischem Schmerz. Zudem tätig als Supervisor und Coach für Teams und Führungskräfte in Kliniken, Verwaltung, Wirtschaft und sozialen Einrichtungen mit Schwerpunkt auf verdeckten Konfliktdynamiken.</p>
  </div>

  <div class="speaker speaker-2 tiny">
    <div class="portrait-shadow"></div>
    <div class="portrait" role="img" aria-label="Porträtfoto der Referentin"></div>
    <h4>Marta Ribeiro Sanz</h4>
    <p>Mediatorin und Prüferin</p>
    <p>Mehrjährige Tätigkeit als Dolmetscherin für internationale Delegationen bei Wirtschaftsgesprächen in mehreren Sprachen. Forschungsaufenthalt an einem sozialwissenschaftlichen Institut im Ausland mit Veröffentlichungen zu Migration und Gesellschaft. Studium der Religionswissenschaft, Soziologie und Politikwissenschaft mit Magisterabschluss. Danach Einstieg als Prüferin bei der Averta GmbH Wirtschaftsprüfungsgesellschaft. Berufsbegleitende Grund- und Aufbauausbildung zur Wirtschaftsmediatorin an einer Mediationsakademie. Heute zertifizierte Mediatorin mit Schwerpunkt auf interkulturellen Konflikten in Unternehmen, Familienbetrieben und Verhandlungen zwischen Partnern.</p>
  </div>

  <div class="speaker speaker-3 tiny">
    <div class="portrait-shadow"></div>
    <div class="portrait" role="img" aria-label="Porträtfoto des Referenten"></div>
    <h4>Jorin Vestergaard</h4>
    <p>Inhaber</p>
    <p>Langjährige Erfahrung im Top-Management als Geschäftsführer und Vorstand, heute gefragter Fachmann als Steuerberater, Wirtschaftsprüfer und Managementberater. Studium der Betriebswirtschaftslehre mit Diplomabschluss. Viele Jahre Partner und Vorstand einer großen Prüfungsgesellschaft, Bestellung zum Steuerberater und Wirtschaftsprüfer. Danach leitende Position in einer internationalen Unternehmensberatung. Heute Inhaber der Averta GmbH Wirtschaftsprüfungsgesellschaft.</p>
  </div>

  <div class="abs references tiny">
    <p>Referenzen für Mandanten aus Wirtschaft und Politik</p>
    <ul>
      <li>Landesparlament, Verkehrsbetriebe, Werften</li>
      <li>Bundesbehörden, Infrastrukturbetreiber</li>
      <li>Industrieunternehmen AG</li>
      <li>Erbschaft und Vermögensnachfolge</li>
      <li>Ligastreit im Profisport</li>
    </ul>
  </div>
</div>

</body>
</html>
```